Business Card Design For Marketing Agnecy LVT

Need business card design for marketing agency.

Dorian Pell
President, CEO
1-555-304-2917
dorian@lumenvaletrewards.net
www.LumenValeTrewards.biz

Back Side:
Boost Sales Using Rewards, Incentives & Giveaways
Get A Free Sample Package

Target Market(s)

B2B

Industry/Entity Type

Marketing

Contact Information for Business Card

Dorian Pell
President, CEO
1-555-304-2917

Back Side:
Get A Free Sample Package

Please note that my current url is OLD DESIGN. I am working on new design and want the business card to match color themes at least on new site. Here is the demo link for new site so you can see the colors I use, etc.

http://pagekilnstudio.example/qx/dorian/lvt_final/index.html

Requirements
Must have
• Please note that my current url is OLD DESIGN. I am working on new design and want the business card to match color themes at least on new site. Here is the demo link for new site so you can see the colors I use, etc.

Nice to have

Should not have

```html
<!DOCTYPE html>
<html lang="en">
<head>
<meta charset="utf-8">
<title>Lumen Vale Trewards Business Card</title>
<link href="https://fonts.googleapis.com/css2?family=Montserrat:wght@400;500;600;700;800&display=swap" rel="stylesheet">
<style>
  :root {
    --brand-blue: #2a7bc4;
    --ink: #333333;
    --paper: #ffffff;
    --dark-top: #4a4a4a;
    --dark-bottom: #282828;
    --light-text: #f2f2f2;
  }
  html, body {
    margin: 0;
    padding: 0;
    width: 1200px;
    height: 840px;
    overflow: hidden;
    background: var(--paper);
    font-family: "Montserrat", sans-serif;
  }
  .canvas {
    position: relative;
    width: 1200px;
    height: 840px;
  }
  .card {
    position: absolute;
    top: 232px;
    width: 364px;
    height: 364px;
    border-radius: 10px;
    box-shadow: 6px 10px 16px rgba(0, 0, 0, 0.28);
    box-sizing: border-box;
    text-align: center;
  }
  .card--front {
    left: 204px;
    background: var(--paper);
    color: var(--ink);
  }
  .card--back {
    left: 632px;
    background: linear-gradient(180deg, var(--dark-top), var(--dark-bottom));
    color: var(--light-text);
  }

  /* Front */
  .front-name {
    position: absolute;
    top: 44px;
    left: 0;
    right: 0;
    color: var(--brand-blue);
    font-weight: 600;
    line-height: 1;
  }
  .front-name__main {
    display: block;
    font-size: 40px;
    letter-spacing: 1px;
  }
  .front-name__sub {
    display: block;
    margin-top: 8px;
    font-size: 17px;
    letter-spacing: 5px;
  }
  .person {
    position: absolute;
    top: 186px;
    left: 0;
    right: 0;
  }
  .person__name {
    margin: 0;
    color: var(--brand-blue);
    font-size: 19px;
    font-weight: 700;
    letter-spacing: 0.5px;
  }
  .person__title {
    margin: 3px 0 0;
    font-size: 13.5px;
    font-weight: 400;
  }
  .contact-icons {
    position: absolute;
    top: 244px;
    left: 0;
    right: 0;
    display: flex;
    justify-content: center;
    gap: 7px;
  }
  .contact-icons svg { width: 15px; height: 15px; }
  .contact-list {
    position: absolute;
    top: 270px;
    left: 0;
    right: 0;
    margin: 0;
    padding: 0;
    list-style: none;
    font-size: 13.5px;
    line-height: 18.5px;
  }

  /* Back */
  .back-brand {
    position: absolute;
    top: 38px;
    left: 0;
    right: 0;
  }
  .back-brand__dot {
    display: block;
    width: 64px;
    height: 64px;
    margin: 0 auto;
    border-radius: 50%;
    background: var(--brand-blue);
  }
  .back-brand__name {
    display: block;
    margin-top: 16px;
    color: var(--brand-blue);
    font-size: 21px;
    font-weight: 600;
    letter-spacing: 1px;
    line-height: 1;
  }
  .tagline {
    position: absolute;
    top: 197px;
    left: 30px;
    right: 30px;
    margin: 0;
    font-size: 14px;
    line-height: 18px;
  }
  .offer {
    position: absolute;
    top: 246px;
    left: 15px;
    width: 334px;
    height: 60px;
  }
  .offer svg { position: absolute; inset: 0; }
  .offer__label {
    position: relative;
    display: block;
    padding-top: 20px;
    color: #ffffff;
    font-size: 14.5px;
    font-weight: 800;
    letter-spacing: 1.2px;
    text-transform: uppercase;
  }
  .back-url {
    position: absolute;
    top: 314px;
    right: 28px;
    margin: 0;
    font-size: 14px;
    letter-spacing: 0.8px;
  }
</style>
</head>
<body>
<main class="canvas">
  <section class="card card--front" aria-label="Card front">
    <div class="front-name">
      <span class="front-name__main">LUMEN VALE</span>
      <span class="front-name__sub">TREWARDS</span>
    </div>
    <div class="person">
      <p class="person__name">DORIAN PELL</p>
      <p class="person__title">President, CEO</p>
    </div>
    <div class="contact-icons" aria-hidden="true">
      <svg viewBox="0 0 16 16"><rect width="16" height="16" rx="2" fill="var(--brand-blue)"/><path d="M5 3.5l2 2-1.2 1.3c.6 1.4 1.6 2.4 3 3L10 8.6l2 2-1 1.9c-3.5-.3-6.6-3.4-7-7z" fill="#fff"/></svg>
      <svg viewBox="0 0 16 16"><rect width="16" height="16" rx="2" fill="var(--brand-blue)"/><rect x="3.5" y="4.5" width="9" height="7" rx="1" fill="none" stroke="#fff" stroke-width="1.2"/><path d="M3.8 5l4.2 3.3L12.2 5" fill="none" stroke="#fff" stroke-width="1.2"/></svg>
      <svg viewBox="0 0 16 16"><rect width="16" height="16" rx="2" fill="var(--brand-blue)"/><circle cx="8" cy="8" r="4.6" fill="none" stroke="#fff" stroke-width="1.1"/><ellipse cx="8" cy="8" rx="2" ry="4.6" fill="none" stroke="#fff" stroke-width="1"/><path d="M3.4 8h9.2M4 5.8h8M4 10.2h8" stroke="#fff" stroke-width="0.9"/></svg>
    </div>
    <ul class="contact-list">
      <li>1-555-304-2917</li>
      <li>www.LumenValeTrewards.biz</li>
      <li>dorian@lumenvaletrewards.net</li>
    </ul>
  </section>

  <section class="card card--back" aria-label="Card back">
    <div class="back-brand">
      <span class="back-brand__dot" aria-hidden="true"></span>
      <span class="back-brand__name">LUMEN VALE TREWARDS</span>
    </div>
    <p class="tagline">Boost Sales Using Rewards, Incentives &amp; Giveaways</p>
    <div class="offer">
      <svg viewBox="0 0 334 60" preserveAspectRatio="none" aria-hidden="true">
        <polygon points="0,2 334,0 328,52 170,52 167,59 164,52 10,53" fill="var(--brand-blue)"/>
      </svg>
      <span class="offer__label">Get a free sample package</span>
    </div>
    <p class="back-url">www.LumenValeTrewards.biz</p>
  </section>
</main>
</body>
</html>
```